a promotional poster design to promote our upcoming event. We want the date to be promoted as "Save the Date" for Sunday 4th July 2021.

Requirements
Must have
• the following text;

Save the Date! (stand out)
Sunday 4th July 2021 (stand out)
KTRB Family Mixed Netball Carnival
Nice to have
• make the date stand out. We want people to lock in the date we're promoting.

```html
<!DOCTYPE html>
<html lang="en">
<head>
<meta charset="utf-8">
<title>Save the Date – Sunday 4th July 2021</title>
<link rel="stylesheet" href="https://fonts.googleapis.com/css2?family=Chewy&family=Montserrat:wght@600;800&display=swap">
<style>
  :root {
    --red: #e31e26;
    --yellow: #f4b91a;
    --white: #ffffff;
    --black: #0b0b0b;
    --ink: #1a1a1a;
    --backdrop: #ecebe8;
  }
  * { margin: 0; padding: 0; box-sizing: border-box; }
  html, body {
    width: 1200px;
    height: 964px;
    overflow: hidden;
    background: var(--backdrop);
  }
  .canvas {
    position: relative;
    width: 1200px;
    height: 964px;
  }
  .poster {
    position: absolute;
    left: 317px;
    top: 22px;
    width: 566px;
    height: 920px;
    box-shadow: 0 10px 30px rgba(0,0,0,0.18);
    background: var(--white);
  }
  .poster svg { display: block; }
  .headline { font-family: "Chewy", system-ui, cursive; }
  .body-type { font-family: "Montserrat", Arial, sans-serif; }
  .fill-red { fill: var(--red); }
  .fill-yellow { fill: var(--yellow); }
  .fill-white { fill: var(--white); }
  .fill-black { fill: var(--black); }
  .fill-ink { fill: var(--ink); }
</style>
</head>
<body>
<main class="canvas">
  <section class="poster" aria-label="Save the Date poster">
    <svg width="566" height="920" viewBox="0 0 566 920" xmlns="http://www.w3.org/2000/svg">
      <!-- red field -->
      <path class="fill-red" d="M0 0 H566 V615 Q300 690 0 590 Z"/>

      <!-- upper divider: thin white line and black swoosh -->
      <path d="M0 295 Q270 430 566 340" fill="none" stroke="var(--white)" stroke-width="2.5"/>
      <path class="fill-black" d="M120 345 Q300 420 566 352 V381 Q320 440 120 345 Z"/>

      <!-- lower divider: black swoosh into white base -->
      <path class="fill-black" d="M0 586 Q260 672 500 603 Q280 690 0 612 Z"/>

      <!-- accent ticks -->
      <path class="fill-white" d="M62 58 L84 100 L72 104 Z"/>
      <path class="fill-white" d="M68 122 L98 116 L96 128 Z"/>
      <path class="fill-white" d="M488 202 L462 236 L472 242 Z"/>
      <path class="fill-white" d="M488 252 L462 248 L466 258 Z"/>

      <!-- headline -->
      <text class="headline fill-white" x="104" y="215" font-size="178" textLength="340" lengthAdjust="spacingAndGlyphs">Save</text>
      <text class="headline fill-white" x="133" y="273" font-size="60" textLength="62" lengthAdjust="spacingAndGlyphs">the</text>
      <text class="headline fill-yellow" x="210" y="336" font-size="140" textLength="250" lengthAdjust="spacingAndGlyphs">Date!</text>

      <!-- date -->
      <text class="body-type fill-white" x="85" y="505" font-size="98" font-weight="800" textLength="400" lengthAdjust="spacingAndGlyphs">SUNDAY</text>
      <rect class="fill-black" x="87" y="510" width="251" height="70"/>
      <text class="body-type fill-white" x="101" y="565" font-size="58" font-weight="800" textLength="82" lengthAdjust="spacingAndGlyphs">4th</text>
      <text class="body-type fill-yellow" x="198" y="565" font-size="58" font-weight="800" textLength="124" lengthAdjust="spacingAndGlyphs">July</text>
      <text class="body-type fill-yellow" x="351" y="572" font-size="72" font-weight="800" textLength="137" lengthAdjust="spacingAndGlyphs">2021</text>

      <!-- host organisation -->
      <circle class="fill-red" cx="172" cy="738" r="40"/>
      <text class="body-type fill-ink" x="172" y="828" font-size="19" font-weight="800" text-anchor="middle" textLength="200" lengthAdjust="spacingAndGlyphs">KTRB COMMUNITY</text>
      <text class="body-type fill-ink" x="172" y="854" font-size="19" font-weight="800" text-anchor="middle" textLength="150" lengthAdjust="spacingAndGlyphs">HEALTH SERVICE</text>
      <text class="body-type fill-yellow" x="172" y="880" font-size="14" font-weight="600" text-anchor="middle">Caring for the Community</text>

      <!-- event name -->
      <text class="body-type fill-red" x="404" y="765" font-size="30" font-weight="800" text-anchor="middle" textLength="190" lengthAdjust="spacingAndGlyphs">KTRB FAMILY</text>
      <text class="body-type fill-red" x="404" y="805" font-size="30" font-weight="800" text-anchor="middle" textLength="200" lengthAdjust="spacingAndGlyphs">MIXED NETBALL</text>
      <text class="body-type fill-red" x="404" y="845" font-size="30" font-weight="800" text-anchor="middle" textLength="160" lengthAdjust="spacingAndGlyphs">CARNIVAL</text>
    </svg>
  </section>
</main>
</body>
</html>
```